Missing Kids Car Doantion Website Design

Please create a new one page website design.

Current site: http://autosforyouth.net/

New WEBSITE address is: VansForLostYouth.org

Use these sites for an idea of what I am looking for. I like these sites best: tiresforsoldiers.org and autosforsoldiers.org

Coding

Coded - Design and coding required

Number of Pages Required

1 page

```html
<!DOCTYPE html>
<html lang="en">
<head>
<meta charset="utf-8">
<title>Give A Ride – Help Find Missing Kids</title>
<link href="https://fonts.googleapis.com/css2?family=Oswald:wght@300;400;500;600&family=Poppins:wght@400;500;600;700&display=swap" rel="stylesheet">
<style>
:root{
  --blue:#2b7fd8;
  --blue-deep:#1f64b8;
  --navy:#0c2a5a;
  --navy-2:#14386f;
  --cyan:#28c3e6;
  --cyan-dark:#1aa8cc;
  --orange:#f7a03c;
  --text:#4a4a4a;
  --heading:#222;
  --pale:#eef6fd;
  --white:#fff;
}
*{box-sizing:border-box;margin:0;padding:0}
html,body{width:1200px;height:3285px;overflow:hidden}
body{font-family:"Poppins",sans-serif;color:var(--text);background:var(--white)}
.wrap{width:1030px;margin:0 auto;position:relative}

/* header */
.site-header{height:66px}
.site-header .wrap{display:flex;align-items:center;justify-content:space-between;height:66px}
.brand{display:flex;flex-direction:column;line-height:1.05}
.brand-name{font-weight:700;font-size:27px;color:var(--blue)}
.brand-tag{font-size:13px;color:var(--blue)}
.nav{display:flex;gap:54px;font-size:15px;color:#333}

/* hero */
.hero{height:526px;position:relative;background:linear-gradient(90deg,#d7d4cf,#c9c6c1 55%,#e2e0dc)}
.hero-photo{position:absolute;left:0;top:0;width:697px;height:526px;background:radial-gradient(circle at 45% 50%,#b4362f 0,#8c6c6a 14%,#cfccc7 36%,#dcd9d4 70%)}
.hero-side{position:absolute;right:0;top:0;width:83px;height:526px;background:linear-gradient(#d8d6d2,#bbb8b3)}
.donate-panel{position:absolute;left:700px;top:0;width:417px;height:526px;background:var(--cyan);color:var(--white);text-align:center}
.pickup{height:59px;background:var(--cyan-dark);font-family:"Oswald",sans-serif;font-size:20px;display:flex;align-items:center;justify-content:center;gap:10px}
.pickup b{font-weight:600}
.donate-panel h1{font-family:"Oswald",sans-serif;font-weight:500;font-size:33px;margin-top:16px}
.donate-panel h2{font-family:"Oswald",sans-serif;font-weight:400;font-size:21px;margin-top:2px}
.donate-panel .lead{font-family:"Oswald",sans-serif;font-size:15px;margin-top:6px}
.boat{display:flex;align-items:center;gap:10px;font-family:"Oswald",sans-serif;font-size:13px;margin:14px 0 0 18px}
.boat span{width:16px;height:16px;border:1.5px solid var(--white);border-radius:50%}
.fields{display:grid;grid-template-columns:1fr 1fr;gap:14px 12px;margin:20px 18px 0;text-align:left}
.fields label{font-size:10px;display:block;margin-bottom:5px}
.fields .box{height:36px;border:1.5px solid rgba(255,255,255,.85)}
.btn{display:inline-block;border-radius:20px;font-family:"Oswald",sans-serif;font-weight:500;color:var(--white);letter-spacing:.5px}
.btn-next{background:var(--blue);font-size:14px;padding:8px 24px;margin-top:24px}

/* alert band */
.alert{height:283px;background:linear-gradient(90deg,#2e6ec4,#3b7fd2 40%,#2f6fc6);position:relative;color:var(--white)}
.alert-photo{position:absolute;left:0;top:0;width:400px;height:283px;background:radial-gradient(circle at 35% 45%,#8fb7e3 0,#5a93d6 30%,rgba(47,111,198,0) 70%)}
.alert-copy{position:absolute;left:436px;top:37px;width:680px}
.alert-copy h3{font-family:"Oswald",sans-serif;font-weight:500;font-size:24px}
.alert-copy h4{font-family:"Oswald",sans-serif;font-weight:500;font-size:17px;margin-top:2px}
.alert-copy p{font-size:14px;margin-top:10px}
.alert-stats{display:flex;gap:22px;margin-top:24px}
.alert-stat{width:158px;height:92px;border:1.5px solid rgba(255,255,255,.75);border-left:5px solid var(--orange);padding:10px 12px;font-family:"Oswald",sans-serif}
.alert-stat b{display:block;font-weight:500;font-size:20px;line-height:1.3}
.alert-stat span{display:block;font-weight:300;font-size:16px;line-height:1.25}

/* about */
.about{height:526px;padding-top:56px}
.about .wrap{display:flex;justify-content:space-between}
.about-text{width:480px}
.section-title{font-family:"Oswald",sans-serif;font-weight:500;font-size:25px;color:var(--heading)}
.rule{width:60px;height:2px;background:var(--orange);margin:10px 0 14px}
.about-text p{font-size:12px;line-height:1.52}
.video{width:500px;height:327px;background:linear-gradient(135deg,#4c6b46,#a69a4f 45%,#e9c23a 70%,#6d7b5c);position:relative}
.video svg{position:absolute;left:50%;top:50%;transform:translate(-50%,-50%)}
.btn-donate{background:var(--orange);font-size:16px;padding:9px 22px;display:flex;align-items:center;gap:8px;width:max-content;margin:34px auto 0}

/* missing kids */
.kids{height:414px;background:linear-gradient(90deg,#6d5a4e,#9c8979 30%,#6f6b70 60%,#a1795a);position:relative;text-align:center}
.kids .section-title{color:var(--white);padding-top:30px}
.kids .rule{margin:8px auto 0}
.kid-row{display:flex;gap:29px;justify-content:center;margin-top:30px}
.kid-card{width:147px;height:265px;background:var(--white);padding:7px}
.kid-photo{height:150px;background:linear-gradient(#c9a48b,#8c6b58)}
.kid-card b{display:block;font-size:12px;color:var(--heading);margin-top:10px}
.kid-card small{display:block;font-size:11px;line-height:1.6;color:#444}
.arrow{position:absolute;top:216px;width:38px;height:38px}
.arrow.left{left:28px}.arrow.right{right:28px}

/* contact */
.contact{height:354px;padding-top:52px;text-align:center}
.contact .rule{margin:8px auto 0}
.contact-grid{display:grid;grid-template-columns:1fr 1fr;gap:56px 30px;margin-top:34px;text-align:left}
.contact-field{display:flex;align-items:flex-end;gap:12px;font-family:"Oswald",sans-serif;font-size:16px;color:#2a3a6a}
.contact-field i{flex:1;border-bottom:1px solid #a8a8b8;height:1px}
.btn-submit{background:var(--orange);font-size:15px;padding:8px 26px;margin-top:34px}

/* numbers */
.numbers{height:340px;background:linear-gradient(90deg,var(--navy),var(--navy-2) 50%,var(--navy));color:var(--white);padding-top:51px}
.number-row{display:flex;justify-content:space-between}
.number{width:327px;height:162px;border:1.5px solid rgba(255,255,255,.5);text-align:center;padding-top:20px;font-family:"Oswald",sans-serif}
.number b{display:block;font-weight:500;font-size:33px}
.number span{display:block;font-size:19px;line-height:1.45;margin-top:6px}
.numbers p{text-align:center;font-family:"Oswald",sans-serif;font-size:14px;line-height:1.8;margin-top:42px}

/* faq */
.faq{height:565px;padding-top:52px;text-align:center}
.faq .rule{margin:8px auto 0}
.faq-body{display:flex;justify-content:space-between;margin-top:46px;text-align:left}
.faq-list{width:502px;display:flex;flex-direction:column}
.faq-item{height:55px;display:flex;align-items:center;background:var(--blue);color:var(--white);font-family:"Oswald",sans-serif;font-size:16px;border-bottom:1px solid #fff;position:relative}
.faq-item .icon{width:44px;height:55px;display:flex;align-items:center;justify-content:center;background:var(--cyan);font-size:24px;margin-right:16px}
.faq-item.open::after{content:"";position:absolute;right:-8px;top:19px;border-top:8px solid transparent;border-bottom:8px solid transparent;border-left:8px solid var(--blue)}
.faq-answer{width:500px;height:377px;background:var(--pale);padding:30px 20px}
.faq-answer h5{font-family:"Oswald",sans-serif;font-weight:400;font-size:19px;color:#333}
.faq-answer .rule{margin:12px 0 16px}
.faq-answer p{font-size:12px;line-height:1.8;margin-bottom:14px}

/* footer */
.site-footer{height:208px;background:var(--navy);color:var(--white);text-align:center;padding-top:26px}
.site-footer h6{font-size:16px;font-weight:600}
.site-footer p{font-size:12px;line-height:1.9;width:1030px;margin:14px auto 0}
.site-footer small{display:block;font-size:11.5px;margin-top:40px;opacity:.85}
</style>
</head>
<body>

<header class="site-header">
  <div class="wrap">
    <div class="brand"><span class="brand-name">Give A Ride</span><span class="brand-tag">Help Find Missing Kids</span></div>
    <nav class="nav"><span>Home</span><span>About</span><span>Seek The Young</span><span>Missing Kids</span><span>Contact</span><span>FAQ</span></nav>
  </div>
</header>

<section class="hero">
  <div class="hero-photo" role="img" aria-label="Photo of a small child sitting on the floor hugging his knees against a white wooden wall"></div>
  <div class="hero-side" role="img" aria-label="Continuation of the wooden wall backdrop"></div>
  <div class="donate-panel">
    <div class="pickup">FAST FREE PICKUP <b>888-555-0142</b></div>
    <h1>DONATE YOUR CAR OR BOAT</h1>
    <h2>2-STEP DONATION - MADE QUICK &amp; EASY</h2>
    <p class="lead">FILL OUT THE FORM &amp; HELP PROTECT THE FUTURE OF CHILDREN.</p>
    <div class="boat"><span></span>DONATE A BOAT INSTEAD</div>
    <div class="fields">
      <div><label>Year</label><div class="box"></div></div>
      <div><label>Make</label><div class="box"></div></div>
      <div><label>Model</label><div class="box"></div></div>
      <div><label>Does it run?</label><div class="box"></div></div>
      <div><label>Do you have the title?</label><div class="box"></div></div>
      <div><label>Any major damage?</label><div class="box"></div></div>
    </div>
    <span class="btn btn-next">NEXT STEP</span>
  </div>
</section>

<section class="alert">
  <div class="alert-photo" role="img" aria-label="Photo of a child's hand pressed against glass with a help note"></div>
  <div class="alert-copy">
    <h3>EVERY 10 MINUTES, THERE'S AN ATTEMPT TO ABDUCT A CHILD.</h3>
    <h4>MOST PARENTS DON'T THINK IT WILL HAPPEN TO THEM.</h4>
    <p>According to the Federal Safety Bureau, each year, there are approximately</p>
    <div class="alert-stats">
      <div class="alert-stat"><b>94,000</b><span>MISSING CHILDREN</span></div>
      <div class="alert-stat"><b>90,000</b><span>RUNAWAYS</span></div>
      <div class="alert-stat"><b>300</b><span>STRANGER<br>ABDUCTIONS</span></div>
      <div class="alert-stat"><b>981</b><span>FAMILY<br>ABDUCTIONS</span></div>
    </div>
  </div>
</section>

<section class="about">
  <div class="wrap">
    <div class="about-text">
      <h2 class="section-title">ABOUT SEEK THE YOUNG</h2>
      <div class="rule"></div>
      <p>Seek The Young is a non-profit corporation dedicated to the recovery of missing children and to the prevention of the abuse and endangerment of children. Seek The Young assists families searching for missing children by helping them to access local and federal law enforcement, advising them on the appropriate legal documents, and connecting them with other non-profit organizations or community resources that may help them in their search for their children. We educate parents and children on child safety, and work closely and in conjunction with the National Registry for Lost Youth. We have bilingual volunteers available to work with Spanish speaking families. Since 1983, Seek The Young has assisted thousands of families by distributing flyers with missing children's pictures on them through our volunteer flyer distribution program and on our stickers which are placed on vending machines.</p>
    </div>
    <div class="video" role="img" aria-label="Video still of a child holding yellow balloons at a playground">
      <svg width="60" height="60" viewBox="0 0 60 60"><circle cx="30" cy="30" r="27" fill="none" stroke="#fff" stroke-width="3"/><path d="M24 18 L42 30 L24 42 Z" fill="#fff"/></svg>
    </div>
  </div>
  <span class="btn btn-donate">DONATE NOW <svg width="16" height="14" viewBox="0 0 16 14"><path d="M8 14 L1.5 7.5 A3.8 3.8 0 0 1 8 2.5 A3.8 3.8 0 0 1 14.5 7.5 Z" fill="#fff"/></svg></span>
</section>

<section class="kids" aria-label="Missing kids">
  <h2 class="section-title">MISSING KIDS</h2>
  <div class="rule"></div>
  <svg class="arrow left" viewBox="0 0 38 38"><circle cx="19" cy="19" r="17" fill="none" stroke="#fff" stroke-width="2"/><path d="M22 12 L15 19 L22 26" fill="none" stroke="#fff" stroke-width="2.5"/></svg>
  <svg class="arrow right" viewBox="0 0 38 38"><circle cx="19" cy="19" r="17" fill="none" stroke="#fff" stroke-width="2"/><path d="M16 12 L23 19 L16 26" fill="none" stroke="#fff" stroke-width="2.5"/></svg>
  <div class="kid-row">
    <div class="kid-card"><div class="kid-photo" role="img" aria-label="Portrait photo of a missing child"></div><b>Marcus Ellery</b><small>City: Los Angeles<br>ABD: 10/19/2017<br>DOB: 9/14/2017</small></div>
    <div class="kid-card"><div class="kid-photo" role="img" aria-label="Portrait photo of a missing child"></div><b>Marcus Ellery</b><small>City: Los Angeles<br>ABD: 10/19/2017<br>DOB: 9/14/2017</small></div>
    <div class="kid-card"><div class="kid-photo" role="img" aria-label="Portrait photo of a missing child"></div><b>Marcus Ellery</b><small>City: Los Angeles<br>ABD: 10/19/2017<br>DOB: 9/14/2017</small></div>
    <div class="kid-card"><div class="kid-photo" role="img" aria-label="Portrait photo of a missing child"></div><b>Marcus Ellery</b><small>City: Los Angeles<br>ABD: 10/19/2017<br>DOB: 9/14/2017</small></div>
    <div class="kid-card"><div class="kid-photo" role="img" aria-label="Portrait photo of a missing child"></div><b>Marcus Ellery</b><small>City: Los Angeles<br>ABD: 10/19/2017<br>DOB: 9/14/2017</small></div>
    <div class="kid-card"><div class="kid-photo" role="img" aria-label="Portrait photo of a missing child"></div><b>Marcus Ellery</b><small>City: Los Angeles<br>ABD: 10/19/2017<br>DOB: 9/14/2017</small></div>
  </div>
</section>

<section class="contact">
  <div class="wrap">
    <h2 class="section-title">CONTACT US</h2>
    <div class="rule"></div>
    <div class="contact-grid">
      <div class="contact-field">FULL NAME<i></i></div>
      <div class="contact-field">PHONE NUMBER<i></i></div>
      <div class="contact-field">EMAIL<i></i></div>
      <div class="contact-field">MESSAGE<i></i></div>
    </div>
    <span class="btn btn-submit">SUBMIT</span>
  </div>
</section>

<section class="numbers">
  <div class="wrap">
    <div class="number-row">
      <div class="number"><b>800,000</b><span>Children are reported missing<br>a year</span></div>
      <div class="number"><b>751,000</b><span>Children have seen the Seek the<br>Young program</span></div>
      <div class="number"><b>400+</b><span>Open missing children<br>cases</span></div>
    </div>
    <p>You can help protect the future of children by supporting Seek The Young through your car donation. Your donated vehicle or vessel will be sold at auction and the net proceeds will<br>be returned to Seek The Young.</p>
  </div>
</section>

<section class="faq">
  <div class="wrap">
    <h2 class="section-title">FREQUENTLY ASKED QUESTIONS</h2>
    <div class="rule"></div>
    <div class="faq-body">
      <div class="faq-list">
        <div class="faq-item"><span class="icon">+</span>WHY DONATE A VEHICLE OR VESSEL?</div>
        <div class="faq-item open"><span class="icon">−</span>HOW DO I DONATE A VEHICLE OR VESSEL?</div>
        <div class="faq-item"><span class="icon">+</span>HOW DOES DONATING A CAR OR BOAT BENEFIT MY TAXES?</div>
        <div class="faq-item"><span class="icon">+</span>WHY DONATE A VEHICLE OR VESSEL?</div>
        <div class="faq-item"><span class="icon">+</span>WHY DONATE A VEHICLE OR VESSEL?</div>
        <div class="faq-item"><span class="icon">+</span>WHY DONATE A VEHICLE OR VESSEL?</div>
        <div class="faq-item"><span class="icon">+</span>WHY DONATE A VEHICLE OR VESSEL?</div>
      </div>
      <div class="faq-answer">
        <h5>Sed ut perspiciatis unde omnis iste natus error</h5>
        <div class="rule"></div>
        <p>Sed ut perspiciatis unde omnis iste natus error sit voluptatem accusantium doloremque laudantium, totam rem aperiam, eaque ipsa quae ab illo inventore veritatis et quasi architecto beatae vitae dicta sunt explicabo. Nemo enim ipsam voluptatem quia voluptas sit aspernatur aut odit aut fugit, sed quia consequuntur</p>
        <p>magni dolores eos qui ratione voluptatem sequi nesciunt. Neque porro quisquam est, qui dolorem ipsum quia dolor</p>
      </div>
    </div>
  </div>
</section>

<footer class="site-footer">
  <h6>Privacy Policy</h6>
  <p>www.autosforyouth.net is not affiliated with WheelaTots, WheelsForTots, AutosForTots, AutosaTots, Civic Drive Autos For Tots, or any other website. Your donation to www.autosforyouth.net will benefit Seek The Young, a registered Non Profit organization that helps find missing children. Seek The Young is not affiliated with autos for tots, autosfortots, autos 4 tots, autos 4 tots, wheels for tots, or wheels 4 tots.</p>
  <small>© Give A Ride for Children 2018. All Rights Reserved</small>
</footer>

</body>
</html>
```